Velmora Partners - website for real estate investment company

Create a bold, modern website that reflects Velmora’s success, professionalism, and credibility.
The design must stand out while maintaining a polished, corporate tone. (bold, but understated)
The client just created a new logo, and the website design must be in sync with the logo design. Information about the logo colors, fonts, and message are in the attached design brief.
Updates

Target Market(s)

b2b: banks, brokers, institutional partners, vendors, and property sellers.

Industry/Entity Type

real estate investment company

Number of Pages Required

1 page

Font styles to use
Sans Serif

Colors

Designer to choose colors to be used in the design.

Requirements
Must have
• 1. homepage design (psd) 2. a top banner image (psd) for a default inner page
Nice to have
• please see attached design brief
Should not have

```html
<!DOCTYPE html>
<html lang="en">
<head>
<meta charset="utf-8">
<title>Velmora Partners — Real Estate Investment</title>
<link href="https://fonts.googleapis.com/css2?family=Barlow:wght@400;500;600;700;800&family=Barlow+Condensed:wght@600;700&family=Inter:wght@400;500&display=swap" rel="stylesheet">
<style>
:root{
  --red:#d8151f;
  --red-deep:#b41c22;
  --ink:#4a4a4a;
  --ink-dark:#3b3b3b;
  --text:#2a2a2a;
  --muted:#6b6b6b;
  --beige-top:#f6f2ea;
  --beige-bottom:#ece2ca;
  --paper:#ffffff;
  --mist:#f3f3f3;
  --ghost:#ececec;
}
*{margin:0;padding:0;box-sizing:border-box}
html,body{width:1200px;height:3263px;overflow:hidden}
body{position:relative;background:var(--mist);font-family:"Barlow",sans-serif;color:var(--text)}
.abs{position:absolute}
.layer{position:absolute;left:0;top:0;width:1200px;height:3263px}

/* nav */
.nav a{position:absolute;top:40px;font:600 13px "Barlow",sans-serif;letter-spacing:.4px;color:#333;text-decoration:none;text-transform:uppercase}
.nav .logo{top:20px;left:522px;font:700 46px "Barlow Condensed",sans-serif;color:var(--ink);letter-spacing:1px}
.nav .contact-btn{position:absolute;left:981px;top:23px;width:147px;height:49px}
.nav .contact-btn span{position:absolute;left:0;top:16px;width:135px;text-align:center;color:#fff;font:700 14px "Barlow",sans-serif;letter-spacing:.6px}

/* hero */
.hero-word{left:150px;top:88px;font:800 232px/1 "Barlow",sans-serif;color:var(--ink);letter-spacing:-6px}
.hero-photo{left:237px;top:253px;width:726px;height:558px}
.tags .tag{position:absolute;left:948px;height:43px;color:#fff;font:700 25px/43px "Barlow",sans-serif;padding-left:8px}

/* story */
.label{font:600 13px "Barlow",sans-serif;letter-spacing:1px;color:#222}
.intro{left:362px;top:946px;width:750px;font:500 22.5px/32px "Inter",sans-serif;color:#222;letter-spacing:-.2px}
.stat-num{font:600 48px/1 "Barlow",sans-serif;color:#222}
.stat-cap{font:400 15px/21px "Barlow",sans-serif;color:#555;letter-spacing:.3px}
.divider{width:1px;height:66px;background:#cfcfcf}
.ghost{font:800 150px/1 "Barlow",sans-serif;color:var(--ghost);letter-spacing:-3px}

/* testimonials */
.section-title{left:99px;top:2196px;font:600 42px/1 "Barlow",sans-serif;color:#222;letter-spacing:.5px}
.card{position:absolute;top:2300px;width:394px;height:260px;background:#fff;border-radius:6px;padding:20px 29px}
.stars{font-size:17px;color:#222;letter-spacing:2px}
.card h3{margin-top:6px;font:600 22px "Barlow",sans-serif;color:#222}
.card p{margin-top:12px;font:400 13.6px/20.5px "Inter",sans-serif;color:#555}
.person{position:absolute;left:29px;top:204px;display:flex;align-items:center;gap:10px}
.avatar{width:42px;height:42px;border-radius:50%;background:linear-gradient(135deg,#c9c2b8,#6d6a66)}
.person b{display:block;font:600 16px "Barlow",sans-serif;color:#222}
.person small{font:400 12px "Barlow",sans-serif;color:#777}

/* footer */
.foot-logo{left:85px;top:2918px;font:700 70px/1 "Barlow Condensed",sans-serif;color:#fff;letter-spacing:1px}
.career{left:98px;top:3038px;width:229px;height:50px}
.career span{position:absolute;left:0;top:17px;width:210px;text-align:center;color:var(--red);font:700 13px "Barlow",sans-serif;letter-spacing:.6px}
.foot-h{font:700 42px/1 "Barlow",sans-serif;color:#fff;letter-spacing:1px}
.foot-t{font:500 24px/30px "Barlow",sans-serif;color:#fff}
.touch{left:796px;top:2812px;font:400 44px/1 "Barlow",sans-serif;color:#fff;letter-spacing:.5px}
.touch b{font-weight:800}
.field{position:absolute;left:794px;width:302px;border:1px solid #6a6a6a;color:#e8e8e8;font:500 17px "Inter",sans-serif;padding:13px 0 0 34px}
.field svg{position:absolute;left:12px;top:16px}
.submit{left:794px;top:3109px;width:302px;height:50px}
.submit span{position:absolute;left:0;top:17px;width:282px;text-align:center;color:#fff;font:700 14px "Barlow",sans-serif;letter-spacing:.6px}
.legal{top:3204px;font:600 12.5px "Barlow",sans-serif;letter-spacing:.3px}
</style>
</head>
<body>

<!-- hero backdrop -->
<svg class="layer" width="1200" height="3263" aria-hidden="true">
  <defs>
    <linearGradient id="beige" x1="0" y1="0" x2="0" y2="1">
      <stop offset="0" stop-color="#f7f4ee"/><stop offset="1" stop-color="#ebe1c8"/>
    </linearGradient>
  </defs>
  <rect x="0" y="0" width="1200" height="910" fill="url(#beige)"/>
  <polygon points="0,908 1200,621 1200,1300 0,1560" fill="#fff"/>
  <rect x="0" y="1290" width="1200" height="300" fill="#fff"/>
  <polygon points="0,1556 1200,1296 1200,1884 0,2141" fill="var(--ink)"/>
</svg>

<!-- navigation -->
<nav class="nav">
  <svg class="abs" style="left:170px;top:38px" width="9" height="9" aria-hidden="true"><polygon points="0,0 9,0 0,9" fill="var(--red)"/></svg>
  <a style="left:175px">Home</a>
  <a style="left:240px">Our Story</a>
  <a style="left:340px">Investment Strategy</a>
  <a class="logo">VELMORA</a>
  <a style="left:692px">What Sets Us Apart</a>
  <a style="left:865px">Our Portfolio</a>
  <div class="contact-btn">
    <svg width="147" height="49" aria-hidden="true"><polygon points="0,0 147,0 122,49 0,49" fill="var(--red)"/></svg>
    <span>CONTACT</span>
  </div>
</nav>

<!-- hero -->
<div class="abs hero-word">VELMORA</div>
<svg class="abs hero-photo" role="img" aria-label="Modern two-storey white villa with glass walls, lit interiors and a lawn edge">
  <defs>
    <linearGradient id="villa" x1="0" y1="0" x2="1" y2="1">
      <stop offset="0" stop-color="#f2f0ec"/><stop offset=".55" stop-color="#c9b79b"/><stop offset="1" stop-color="#5b5a55"/>
    </linearGradient>
  </defs>
  <polygon points="300,0 520,70 700,120 726,400 640,520 380,558 0,470 0,300 60,120" fill="url(#villa)"/>
</svg>

<svg class="abs" style="left:124px;top:416px" width="114" height="114" role="img" aria-label="Watch our video">
  <defs><path id="ring" d="M57,57 m-46,0 a46,46 0 1,1 92,0 a46,46 0 1,1 -92,0"/></defs>
  <text font-family="Barlow" font-weight="700" font-size="12" letter-spacing="7" fill="#333">
    <textPath href="#ring" startOffset="2%">WATCH • OUR VIDEO •</textPath>
  </text>
  <polygon points="46,40 74,57 46,74" fill="none" stroke="var(--red)" stroke-width="2.5" stroke-linejoin="round"/>
</svg>

<div class="tags">
  <svg class="abs" style="left:948px;top:378px" width="202" height="212" aria-hidden="true">
    <polygon points="0,0 202,0 160,43 0,43" fill="var(--ink)"/>
    <polygon points="0,47 158,47 116,90 0,90" fill="var(--ink)"/>
    <polygon points="0,94 112,94 70,137 0,137" fill="var(--ink)"/>
    <polygon points="0,141 68,141 0,210" fill="var(--red)"/>
  </svg>
  <div class="tag" style="top:378px">EXPERIENCE</div>
  <div class="tag" style="top:425px">STRATEGY</div>
  <div class="tag" style="top:472px">VISION</div>
</div>

<!-- our story -->
<svg class="abs" style="left:85px;top:944px" width="42" height="42" aria-hidden="true"><polygon points="0,0 42,0 0,42" fill="var(--red)"/></svg>
<div class="abs label" style="left:99px;top:957px">OUR STORY</div>
<p class="abs intro">Velmora Partners is a vertically integrated real estate investment firm with a proven four-decade track record. We acquire, reposition, and operate high-performing assets across multiple sectors — always with a focus on exceptional, risk-adjusted returns.</p>

<div class="abs" style="left:361px;top:1137px"><div class="stat-num">1989</div><div class="stat-cap">Founded</div></div>
<div class="abs divider" style="left:546px;top:1132px"></div>
<div class="abs" style="left:623px;top:1137px"><div class="stat-num">23,000+</div><div class="stat-cap">Multifamily &amp;<br>healthcare units</div></div>
<div class="abs divider" style="left:881px;top:1132px"></div>
<div class="abs" style="left:957px;top:1137px"><div class="stat-num">$300+</div><div class="stat-cap">Million invested<br>in renovations</div></div>

<div class="abs ghost" style="left:64px;top:1248px">OUR STORY</div>
<svg class="abs" style="left:513px;top:1261px" width="24" height="24" aria-hidden="true"><polygon points="0,0 24,0 0,24" fill="var(--red)"/></svg>

<!-- gallery -->
<svg class="layer" width="1200" height="3263" aria-hidden="true">
  <defs>
    <linearGradient id="sky" x1="0" y1="0" x2="0" y2="1"><stop offset="0" stop-color="#5d9ad4"/><stop offset=".45" stop-color="#c8d9ea"/><stop offset="1" stop-color="#3d4148"/></linearGradient>
    <linearGradient id="lobby" x1="0" y1="0" x2="0" y2="1"><stop offset="0" stop-color="#bfbfbd"/><stop offset=".5" stop-color="#8a8a87"/><stop offset="1" stop-color="#e1e1df"/></linearGradient>
    <linearGradient id="dusk" x1="0" y1="0" x2="0" y2="1"><stop offset="0" stop-color="#c9a27c"/><stop offset=".45" stop-color="#e9b98a"/><stop offset="1" stop-color="#4e4a48"/></linearGradient>
  </defs>
</svg>
<svg class="layer" width="1200" height="3263">
  <polygon role="img" aria-label="City skyline with a tall glass tower under a blue sky" points="85,1584 416,1505 416,2015 85,2082" fill="url(#sky)"/>
  <polygon role="img" aria-label="Marble office lobby corridor with elevators" points="436,1508 765,1429 765,1938 436,2008" fill="url(#lobby)"/>
  <polygon role="img" aria-label="Manhattan-style skyline at sunset" points="784,1425 1115,1353 1115,1865 784,1935" fill="url(#dusk)"/>
  <g stroke="#fff" stroke-width="2" fill="none" aria-hidden="true">
    <path d="M574,1742 L624,1695 M610,1695 L624,1695 L624,1709 M574,1742 M576,1728 L576,1742 L590,1742"/>
  </g>
</svg>

<!-- testimonials -->
<div class="abs ghost" style="left:622px;top:2012px">CLIENT</div>
<svg class="abs" style="left:1083px;top:2031px" width="23" height="23" aria-hidden="true"><polygon points="0,0 23,0 0,23" fill="var(--red)"/></svg>

<svg class="abs" style="left:85px;top:2192px" width="42" height="42" aria-hidden="true"><polygon points="0,0 42,0 0,42" fill="var(--red)"/></svg>
<h2 class="abs section-title">WHAT OUR CLIENT SAY</h2>

<svg class="abs" style="left:1027px;top:2196px" width="90" height="36" aria-hidden="true">
  <polygon points="0,0 36,0 0,36" fill="none" stroke="#c9c9c9"/>
  <path d="M10,17 H36 M10,17 L17,11 M10,17 L17,23" stroke="#333" stroke-width="1.5" fill="none"/>
  <polygon points="54,0 90,0 90,36" fill="var(--red)"/>
  <path d="M50,17 H80 M80,17 L73,11 M80,17 L73,23" stroke="#222" stroke-width="1.5" fill="none"/>
</svg>

<article class="card" style="left:85px">
  <div class="stars">★★★★★</div>
  <h3>Highly recommend!</h3>
  <p>Lorem ipsor sit amet, consectetur adipiscing elit, sed do eiusmod tempor incididunt ut labore et dolore magna aliqua. Quis ipsum suspendisse ulces gravida. Maecenas lectus metus, gravida sed.</p>
  <div class="person"><div class="avatar" role="img" aria-label="Client portrait"></div><div><b>Alex Smith</b><small>Client</small></div></div>
</article>
<article class="card" style="left:512px">
  <div class="stars">★★★★★</div>
  <h3>Very happy to connect with Velmora</h3>
  <p>Lorem ipsor sit amet, consectetur adipiscing elit, sed do eiusmod tempor incididunt ut labore et dolore magna aliqua. Quis ipsum suspendisse ulces gravida. Maecenas lectus metus, gravida sed.</p>
  <div class="person"><div class="avatar" role="img" aria-label="Client portrait"></div><div><b>Jenifar Wilson</b><small>Client</small></div></div>
</article>
<article class="card" style="left:939px">
  <div class="stars">★★★★★</div>
  <h3>Highly recommend!</h3>
  <p>Lorem ipsor sit amet, consectetur adipiscing elit, sed do eiusmod tempor incididunt ut labore et dolore magna aliqua. Quis ipsum suspendisse ulces gravida. Maecenas lectus metus, gravida sed.</p>
  <div class="person"><div class="avatar" role="img" aria-label="Client portrait"></div><div><b>Michele Doe</b><small>Client</small></div></div>
</article>

<div class="abs ghost" style="left:82px;top:2598px">REVIEW</div>

<!-- footer -->
<svg class="layer" width="1200" height="3263" aria-hidden="true">
  <polygon points="741,2673 1200,2578 1200,3263 741,3263" fill="var(--ink-dark)"/>
  <polygon points="0,2882 741,2724 741,3263 0,3263" fill="var(--red-deep)"/>
</svg>

<div class="abs foot-logo">VELMORA</div>
<div class="abs career">
  <svg width="229" height="50" aria-hidden="true"><polygon points="0,0 229,0 204,50 0,50" fill="#fff"/></svg>
  <span>✉ CAREER INQUIRIES</span>
</div>

<div class="abs foot-h" style="left:440px;top:2924px">LOCATION</div>
<div class="abs foot-t" style="left:440px;top:2985px">2140 Harbor Rd, Eastbrook,<br>NJ 07990</div>
<div class="abs foot-h" style="left:440px;top:3077px">CONTACT US</div>
<div class="abs foot-t" style="left:440px;top:3126px">info@velmora.com</div>

<svg class="abs" style="left:794px;top:2808px" width="26" height="26" aria-hidden="true"><polygon points="0,0 26,0 0,26" fill="var(--red)"/></svg>
<h2 class="abs touch">GET IN <b>TOUCH</b></h2>

<div class="field" style="top:2880px;height:51px">
  <svg width="13" height="14" aria-hidden="true"><circle cx="6.5" cy="4" r="3.5" fill="#aaa"/><path d="M0,14 a6.5,6 0 0,1 13,0z" fill="#aaa"/></svg>Name</div>
<div class="field" style="top:2942px;height:52px">
  <svg width="15" height="12" aria-hidden="true"><rect width="15" height="11" rx="1" fill="#aaa"/><path d="M0,1 L7.5,6 L15,1" stroke="#3b3b3b" fill="none"/></svg>Email</div>
<div class="field" style="top:3004px;height:95px">
  <svg width="14" height="14" aria-hidden="true"><rect x=".5" y="2.5" width="11" height="11" fill="none" stroke="#aaa"/><path d="M6,8 L13,1" stroke="#aaa" stroke-width="2"/></svg>Message</div>
<div class="abs submit">
  <svg width="302" height="50" aria-hidden="true"><polygon points="0,0 302,0 274,50 0,50" fill="var(--red)"/></svg>
  <span>SUBMIT</span>
</div>

<div class="abs legal" style="left:85px;color:#f0c9cb">© 2025 <b style="color:#fff">VELMORA PARTNERS</b>. ALL RIGHT RESERVED</div>
<div class="abs legal" style="right:85px;color:#8a8a8a">AUGUST 13, 2025. LAYOUT_4</div>

</body>
</html>
```